Brightwell Power Systems

We'd like a web design that's beautiful and professional. We replace existing inefficient systems (mostly lighting at the moment but expanding) with highly efficient systems.

```html
<!DOCTYPE html>
<html lang="en">
<head>
<meta charset="utf-8">
<title>Brightwell Power Systems — LED Lighting Solutions</title>
<link href="https://fonts.googleapis.com/css2?family=Open+Sans:wght@300;400;600;700&display=swap" rel="stylesheet">
<style>
:root{
  --green:#1b8a3d;
  --page:#ebebeb;
  --ink:#333;
  --rule:#cfcfcf;
  --white:#fff;
  --footer:#353535;
  --bubble:#8d8f93;
}
*{margin:0;padding:0;box-sizing:border-box}
html,body{width:686px;height:1200px;overflow:hidden}
body{position:relative;background:var(--page);font-family:"Open Sans",Arial,sans-serif;color:var(--ink)}
.abs{position:absolute}
.top-bar{left:0;top:0;width:686px;height:3px;background:var(--green)}

/* header */
.brand{left:58px;top:34px;display:flex;align-items:center;gap:7px}
.brand-mark{width:22px;height:22px;background:var(--green)}
.brand-name{font-size:12px;font-weight:600;color:var(--green);line-height:1.15;width:96px}
.header-info{left:222px;top:26px;width:260px;text-align:center}
.header-title{font-size:11.5px;color:#777}
.header-title b{color:var(--green);font-weight:400}
.support{margin-top:6px;font-size:7.5px;color:#999;display:flex;justify-content:center;align-items:center;gap:8px}
.support strong{color:#444;font-weight:400}
.benefits{margin-top:4px;font-size:7px;color:#777}
.flag{left:558px;top:20px;width:72px;height:40px;background:linear-gradient(135deg,#2a3f8f 0 40%,#c8333b 40% 100%);border-radius:2px}
.independence{left:548px;top:66px;width:92px;text-align:center;font-size:8.5px;color:#666;line-height:1.3}

/* nav */
.nav{left:58px;top:105px;width:571px;height:34px;background:var(--white);box-shadow:0 1px 2px rgba(0,0,0,.12);display:flex;align-items:center}
.nav a{font-size:9.5px;color:#999;text-decoration:none;padding:0 12px;line-height:34px}
.nav a.active{background:var(--green);color:var(--white);width:80px;text-align:center;padding:0}
.nav .search{margin-left:auto;border-left:1px solid #ccc;height:18px;width:143px;display:flex;align-items:center;justify-content:space-between;padding:0 12px 0 16px;font-size:9px;font-style:italic;color:#aaa}

/* hero */
.hero{left:58px;top:149px;width:571px;height:250px;border:2px solid var(--white);box-shadow:0 2px 4px rgba(0,0,0,.15);background:linear-gradient(180deg,#d9c7ad 0%,#b79a7a 45%,#2b3f7a 70%,#6a5441 100%)}
.hero-arrow{top:117px;width:18px;height:18px;border-radius:50%;background:rgba(255,255,255,.45)}
.hero-caption{left:40px;top:176px;width:212px;height:33px;background:rgba(27,138,61,.9);color:var(--white);font-size:14px;font-weight:300;line-height:33px;padding-left:12px}
.hero-dots{left:260px;top:233px;display:flex;gap:8px}
.hero-dots span{width:9px;height:9px;border-radius:50%;background:#bbb;border:2px solid #eee}
.hero-dots span.on{background:var(--green)}

/* who we are */
.audit{left:58px;top:430px;width:118px;height:91px;background:linear-gradient(135deg,#5b4a42,#c4a58e 60%,#e8d9cc)}
.audit-band{left:0;bottom:4px;width:118px;height:20px;background:rgba(200,200,200,.9);font-size:9px;font-weight:700;font-variant:small-caps;color:#333;line-height:20px;padding-left:9px;white-space:nowrap;overflow:hidden}
h2{font-size:14px;font-weight:400;color:#333}
h2 span{color:var(--green)}
.who-title{left:192px;top:424px}
.who-rule{left:192px;top:449px;width:437px;height:1px;background:var(--rule)}
.who-text{left:58px;top:462px;width:571px;font-size:7.2px;line-height:11.6px;color:#777;text-align:justify}
.who-text .indent{display:block;padding-left:134px}

/* bottom line */
.bottom-title{left:0;top:596px;width:686px;text-align:center}
.bottom-sub{left:120px;top:627px;width:446px;text-align:center;font-size:7px;line-height:12px;color:#999}
.card{top:681px;width:126px}
.card-img{width:126px;height:97px;border:2px solid #d6d6d6}
.card h3{font-size:9px;font-weight:400;text-align:center;margin-top:9px;color:#333}
.card hr{border:0;border-top:1px solid var(--rule);margin-top:8px}
.card p{margin-top:7px;font-size:7px;line-height:12px;color:#999;text-align:justify;text-align-last:center}

/* unique */
.unique-title{left:58px;top:886px}
.unique-list{left:58px;top:925px;width:340px;list-style:none}
.unique-list li{position:relative;padding-left:17px;font-size:7.2px;line-height:15.5px;color:#555}
.unique-list li::before{content:"";position:absolute;left:0;top:4px;width:7px;height:7px;border-radius:50%;background:#aaa}

/* testimonials */
.say-title{left:419px;top:889px}
.testimonial{left:419px;width:210px;height:60px}
.avatar{left:1px;top:0;width:38px;height:38px;border-radius:50%;background:radial-gradient(circle,#cdb7a6,#8e7f76);border:3px solid var(--white);box-shadow:0 0 0 1px #ccc}
.person{left:0;top:42px;width:60px;font-size:5.5px;color:#333;line-height:7px;white-space:nowrap}
.person b{font-weight:700}
.bubble{left:62px;top:0;width:148px;height:54px;background:var(--bubble);border-radius:3px;box-shadow:0 2px 0 #c5c5c5;color:var(--white);font-size:7px;line-height:11.5px;padding:8px 8px;text-align:justify}
.bubble::before{content:"";position:absolute;left:-7px;top:0;border-top:8px solid var(--bubble);border-left:8px solid transparent}

/* footer */
.footer{left:0;top:1144px;width:686px;height:56px;background:var(--footer)}
.footer-links{left:58px;top:16px;display:flex;gap:9px;font-size:7.5px;color:#ddd}
.copyright{left:58px;top:32px;font-size:7.5px;color:#ddd}
.social{left:513px;top:19px;display:flex;gap:7px}
.social span{width:18px;height:18px;border-radius:50%;background:var(--white);display:flex;align-items:center;justify-content:center}
.social svg{width:10px;height:10px}
</style>
</head>
<body>
<div class="abs top-bar"></div>

<header>
  <div class="abs brand"><div class="brand-mark"></div><div class="brand-name">Brightwell Power Systems</div></div>
  <div class="abs header-info">
    <div class="header-title"><b>LED</b> Lighting Solutions</div>
    <div class="support"><span>24/7 Support: <strong>1 (555)-310-482716</strong></span>
      <svg width="20" height="20" viewBox="0 0 20 20" fill="none" stroke="#555" stroke-width="1.3"><path d="M4 11V9a6 6 0 0 1 12 0v2"/><rect x="2.5" y="10" width="3" height="5" rx="1"/><rect x="14.5" y="10" width="3" height="5" rx="1"/><path d="M16 15c0 2-2 3-5 3"/></svg>
    </div>
    <div class="benefits">Better light | Much lower utility bills | Environmentally friendly</div>
  </div>
  <div class="abs flag" role="img" aria-label="Waving national flag graphic"></div>
  <div class="abs independence">Promoting Energy Independence</div>
</header>

<nav class="abs nav">
  <a class="active" href="#">Home</a>
  <a href="#">Why LED?</a>
  <a href="#">Case Studies</a>
  <a href="#">FAQ</a>
  <a href="#">Energy Audit</a>
  <div class="search"><span>Search</span>
    <svg width="9" height="9" viewBox="0 0 10 10" fill="none" stroke="#888" stroke-width="1.3"><circle cx="4.2" cy="4.2" r="3"/><path d="M6.5 6.5L9 9"/></svg>
  </div>
</nav>

<section class="abs hero" role="img" aria-label="Modern living room lit by recessed LED ceiling lights with blue accent lighting">
  <div class="abs hero-arrow" style="left:22px"></div>
  <div class="abs hero-arrow" style="left:531px"></div>
  <div class="abs hero-caption">LED for every applicvation</div>
  <div class="abs hero-dots"><span class="on"></span><span></span><span></span></div>
</section>

<section>
  <div class="abs audit" role="img" aria-label="Consultant meeting a smiling client">
    <div class="abs audit-band">Request A Free Audit</div>
  </div>
  <h2 class="abs who-title">Who <span>We Are</span></h2>
  <div class="abs who-rule"></div>
  <p class="abs who-text"><span class="indent">Brightwell Power Systems is an acknowledged Green Energy leader providing energy saving lighting solutions. Our LEED trained professionals coupled with our close relationships with the leading LED manufacturers around the world, that your LED retrofit project will be affordable; saving you up to 75% on your lighting costs and drastically reducing replacement costs. Our turn-key system takes care of everything from the initial lighting energy audit, to an energy saving solution, to professional installation, and finally complete cleanup and proper disposal. ensures that your LED retrofit project will be affordable; saving you up to 75% on your lighting costs and drastically reducing replacement costs.</span>Our turn-key system takes care of everything from the initial lighting energy audit, to an energy saving solution, to professional installation, and finally complete cleanup and proper disposal.</p>
</section>

<section>
  <h2 class="abs bottom-title">Thw <span>Bottom Line</span></h2>
  <p class="abs bottom-sub">Lorem ipsum dolor sit amet, consectetur adipiscing elit. Praesent justo ligula, interdum ut lobortis quis, interdum vitae metus.<br>Proin fringilla metus non nulla cursus, sit amet rutrum est pretium.</p>

  <article class="abs card" style="left:58px">
    <div class="card-img" role="img" aria-label="Crystal LED bulb resting on banknotes" style="background:radial-gradient(circle at 50% 30%,#e8e8e8,#4a4a3a 70%)"></div>
    <h3>The Savings</h3><hr>
    <p>Lorem ipsum dolor sit amet all cons ectetur adipiscing elit. Un quisque sodales sit amet.</p>
  </article>
  <article class="abs card" style="left:205px">
    <div class="card-img" role="img" aria-label="Hand fitting an LED lamp into a ceiling fixture" style="background:linear-gradient(180deg,#f2f2f2,#d9d9d9)"></div>
    <h3>LED Retrofit Process</h3><hr>
    <p>Lorem ipsum dolor sit amet all cons ectetur adipiscing elit. Un quisque sodales sit amet.</p>
  </article>
  <article class="abs card" style="left:352px">
    <div class="card-img" role="img" aria-label="Calculator on a financial document" style="background:linear-gradient(150deg,#b7c4cf,#5a6b7c 60%,#dfe5ea)"></div>
    <h3>Tax Incentives</h3><hr>
    <p>Lorem ipsum dolor sit amet all cons ectetur adipiscing elit. Un quisque sodales sit amet.</p>
  </article>
  <article class="abs card" style="left:498px">
    <div class="card-img" role="img" aria-label="Clear light bulb against a blue background" style="background:radial-gradient(circle at 50% 45%,#a9c8e2,#3f7cb0 80%)"></div>
    <h3>Utility Rebates</h3><hr>
    <p>Lorem ipsum dolor sit amet all cons ectetur adipiscing elit. Un quisque sodales sit amet.</p>
  </article>
</section>

<section>
  <h2 class="abs unique-title">Why We Are <span>Unique</span></h2>
  <ul class="abs unique-list">
    <li>Established in 1986 with 25 years of outstanding service, a GSA approved vendor</li>
    <li>A Service-Disabled Veteran-Owned company focused on hiring Service Disabled Veterans, Veterans and family members of veterans</li>
    <li>As a member of the National Green Building Alliance, we support green design, construction and operations</li>
    <li>LEED (Leadership in Energy &amp; Environmental Design) trained employees</li>
    <li>DUNS Number - 480273615</li>
    <li>CAGE Code - 7K2R9</li>
    <li>Active in System for Award Management (SAM) - Registration valid until 07/15/2014</li>
    <li>Registered NAICS codes - 238210, 335110, 335122</li>
    <li>LED products available on GSA Schedule - GS-07F-0418M</li>
  </ul>
</section>

<section>
  <h2 class="abs say-title">What people <span>say</span></h2>
  <div class="abs testimonial" style="top:937px">
    <div class="abs avatar" role="img" aria-label="Customer portrait"></div>
    <div class="abs person"><b>DANA REYES</b><br>CEO, LUMAVO.TEST</div>
    <div class="abs bubble">Because we know you don't want to be limited on a portrait or scape format we made Showcase.</div>
  </div>
  <div class="abs testimonial" style="top:1018px">
    <div class="abs avatar" role="img" aria-label="Customer portrait"></div>
    <div class="abs person"><b>DANA REYES</b><br>CEO, LUMAVO.TEST</div>
    <div class="abs bubble">Because we know you don't want to be limited on a portrait or scape format we made Showcase.</div>
  </div>
</section>

<footer class="abs footer">
  <div class="abs footer-links"><span>Contact Us</span><span>Privacy &amp; Security</span><span>Terms of Use</span><span>Opt-out</span></div>
  <div class="abs copyright">Copyright 2014 Brightwell Power Systems All Rights Rights Reserved</div>
  <div class="abs social" aria-label="Social links">
    <span><svg viewBox="0 0 10 10" fill="none" stroke="#1b8a3d" stroke-width="1.3"><rect x="1" y="2" width="8" height="6" rx="1"/><path d="M1 2.5l4 3 4-3"/></svg></span>
    <span><svg viewBox="0 0 10 10" fill="#1b8a3d"><path d="M1.5 2h7a1 1 0 0 1 1 1v3.5a1 1 0 0 1-1 1H5l-2.5 2v-2h-1a1 1 0 0 1-1-1V3a1 1 0 0 1 1-1z"/></svg></span>
    <span><svg viewBox="0 0 10 10" fill="none" stroke="#1b8a3d" stroke-width="1.3"><circle cx="2" cy="8" r="1" fill="#1b8a3d" stroke="none"/><path d="M1.5 4.5a4 4 0 0 1 4 4M1.5 1.5a7 7 0 0 1 7 7"/></svg></span>
    <span><svg viewBox="0 0 10 10" fill="#1b8a3d"><path d="M3 2l5.5 3L3 8z"/></svg></span>
    <span><svg viewBox="0 0 10 10" fill="none" stroke="#1b8a3d" stroke-width="1.3"><circle cx="2.5" cy="5" r="1.2"/><circle cx="7.5" cy="2.5" r="1.2"/><circle cx="7.5" cy="7.5" r="1.2"/><path d="M3.6 4.4l2.8-1.4M3.6 5.6l2.8 1.4"/></svg></span>
  </div>
</footer>
</body>
</html>
```